Business Card design for Property Developer

We need a business card design for a Melbourne based Property Developer called "Kestrelmoor Holdings Pty Ltd".

We subdivide land and onsell to builders etc.

We already have a company logo, which is attached. Also I have attached the layout requirements from the printer. We would like a 2-sided design with one side displaying our logo by itself and the other with the required info, such as name, address, tel no., email, abn etc. The card will need to be used by 4 members of staff so name and contact details should be interchangable.
Updates

If possible, can you please write "name' "job position" "phone" "email" "address" on the card but leave them so I can add the details at a later time. Thank you. Also I plan on printing with UV spot printing as a background on the card. Keep this is mind when designing.

Thanks again.

Hello designers, please do not include pics of houses, house plansĀ or construction machinery etc as we really do not like the way it looks. Thank you.

Target Market(s)

Real Estate Agents, Land Owners, Local Council Departments, Govt Bodies, other Developers etc.

Industry/Entity Type

Business

Requirements
Must have
• 2-sided design with one side displaying our logo by itself and the other with the required info, such as name, address, tel no., email, abn etc.

```html
<!DOCTYPE html>
<html lang="en">
<head>
<meta charset="utf-8">
<title>Kestrelmoor Holdings – Business Card</title>
<link href="https://fonts.googleapis.com/css2?family=Source+Sans+3:wght@400;600;700&display=swap" rel="stylesheet">
<style>
  :root {
    --backdrop: #e9e4df;
    --card: #ffffff;
    --brand-red: #a3191e;
    --band-dark: #9c1a1f;
    --band-bright: #e3222a;
    --brand-blue: #1f3f9a;
    --mark-blue: #2f6fc4;
    --ink: #2b2b2b;
  }
  * { margin: 0; padding: 0; box-sizing: border-box; }
  html, body {
    width: 1200px; height: 900px; overflow: hidden;
    background: var(--backdrop);
    font-family: "Source Sans 3", "Myriad Pro", Arial, sans-serif;
  }
  .canvas { position: relative; width: 1200px; height: 900px; }
  .card {
    position: absolute; top: 298px;
    width: 488px; height: 305px;
    background: var(--card);
    box-shadow: 0 2px 6px rgba(0,0,0,.18);
    overflow: hidden;
  }
  .card--front { left: 94px; }
  .card--back { left: 620px; }

  .brand {
    position: absolute; display: flex; flex-direction: column; align-items: center;
    transform: translateX(-50%);
  }
  .brand__dot { border-radius: 50%; background: var(--mark-blue); }
  .brand__name {
    color: var(--brand-red); font-weight: 700; text-transform: uppercase;
    white-space: nowrap; letter-spacing: .5px;
  }
  .card--front .brand { left: 369px; top: 23px; }
  .card--front .brand__dot { width: 70px; height: 70px; margin-bottom: 12px; }
  .card--front .brand__name { font-size: 15px; }
  .card--back .brand { left: 245px; top: 69px; }
  .card--back .brand__dot { width: 106px; height: 106px; margin-bottom: 16px; }
  .card--back .brand__name { font-size: 24px; }

  .contact { position: absolute; left: 18px; top: 119px; color: var(--ink); }
  .contact__name { font-size: 21px; font-weight: 700; color: var(--brand-red); line-height: 22px; }
  .contact__role { font-size: 14px; line-height: 18px; }
  .contact__company { font-size: 15px; font-weight: 700; color: var(--brand-blue); margin-top: 6px; line-height: 20px; }
  .contact__address { font-size: 14.5px; line-height: 20px; }
  .contact__lines { margin-top: 8px; font-size: 14.5px; line-height: 20px; }
  .contact__line { display: flex; align-items: center; gap: 3px; }
  .contact__line svg { width: 14px; height: 12px; fill: var(--brand-red); }

  .band {
    position: absolute; left: 0; bottom: 0; width: 100%; height: 25px;
    background: linear-gradient(90deg, var(--band-dark), var(--band-bright));
    display: flex; align-items: center; justify-content: center;
  }
  .band__web { color: #fff; font-size: 13px; letter-spacing: 2.4px; }
</style>
</head>
<body>
<main class="canvas">
  <section class="card card--front">
    <div class="brand">
      <span class="brand__dot"></span>
      <span class="brand__name">Kestrelmoor Holdings</span>
    </div>
    <div class="contact">
      <p class="contact__name">Adrian Kell</p>
      <p class="contact__role">Company Director</p>
      <p class="contact__company">Kestrelmoor Holdings Pty Ltd</p>
      <p class="contact__address">17 Larkfield Lane, Brunswick<br>Victoria VIC 3056</p>
      <div class="contact__lines">
        <p class="contact__line">
          <svg viewBox="0 0 14 12" aria-hidden="true"><path d="M1 3.5C1 2 3 1 7 1s6 1 6 2.5v1H10V3.2H4v1.3H1z"/><path d="M3.5 5h7l2 6h-11z"/></svg>
          <span>:0412-555-0187</span>
        </p>
        <p class="contact__line">
          <svg viewBox="0 0 14 12" aria-hidden="true"><path d="M1 2h12v9H1z" fill="none" stroke="#a3191e" stroke-width="1.3"/><path d="M1 2l6 5 6-5M1 11l4.5-4.5M13 11l-4.5-4.5" fill="none" stroke="#a3191e" stroke-width="1.1"/></svg>
          <span>: adrian@kestrelmoor.com</span>
        </p>
      </div>
    </div>
    <div class="band"></div>
  </section>

  <section class="card card--back">
    <div class="brand">
      <span class="brand__dot"></span>
      <span class="brand__name">Kestrelmoor Holdings</span>
    </div>
    <div class="band"><span class="band__web">www.kestrelmoor.com</span></div>
  </section>
</main>
</body>
</html>
```